Stylish new business card needed!

Hello everyone! I am in need of a new business card design for an alarm company here in Hurricane WV. I have all fonts, color codes and logos provided for you use! We are a young company and like the style of a clean sleek looking business card. Would like it double sided, one side holding the logo and the other with your design!
Target Market(s)
The people that are looking for the newest tech for home automation and security
Industry/Entity Type
Alarm services; Home automation
Contact Information for Business Card
Name of person; position (Sales; Installer); Phone Number (555.418.7290); Employee cell Number; Website (www.GuardedByVemlo.example); Employee Email; Double sided
Look and feel
Each slider illustrates characteristics of the customer's brand and the style your logo design should communicate.

```html
<!DOCTYPE html>
<html lang="en">
<head>
<meta charset="utf-8">
<title>Vemlo Business Card</title>
<link rel="stylesheet" href="https://fonts.googleapis.com/css2?family=Lato:wght@400;700;900&display=swap">
<style>
  :root {
    --orange: #f28a45;
    --grey: #999999;
    --grey-text: #6f6f6f;
    --white: #ffffff;
    --backdrop: #2f3236;
  }
  * { box-sizing: border-box; margin: 0; padding: 0; }
  html, body { width: 1200px; height: 952px; overflow: hidden; }
  body {
    background: var(--backdrop);
    font-family: "Lato", sans-serif;
    display: flex; flex-direction: column; align-items: center; justify-content: center; gap: 48px;
  }
  .card {
    position: relative; width: 700px; height: 400px;
    border-radius: 26px; overflow: hidden; background: var(--white);
    box-shadow: 0 10px 30px rgba(0,0,0,.35);
  }
  .brand { display: flex; align-items: center; gap: 14px; font-weight: 700; letter-spacing: 6px; }
  .brand-dot { width: 42px; height: 42px; border-radius: 50%; background: var(--orange); }

  /* logo side */
  .card-back .tab { position: absolute; width: 30px; height: 150px; background: var(--orange); border-radius: 0 14px 14px 0; }
  .card-back .tab-top { left: 0; top: 36px; }
  .card-back .tab-bottom { right: 0; bottom: 36px; border-radius: 14px 0 0 14px; }
  .card-back .brand { position: absolute; inset: 0; justify-content: center; font-size: 72px; color: var(--grey); }

  /* contact side */
  .card-front .panel { position: absolute; left: 0; top: 0; bottom: 0; width: 370px; background: var(--grey); }
  .card-front .brand { position: absolute; left: 60px; top: 90px; font-size: 60px; color: var(--white); }
  .card-front .icon-tab {
    position: absolute; left: 316px; top: 228px; width: 68px; height: 150px;
    background: var(--orange); border-radius: 30px;
    display: flex; flex-direction: column; align-items: center; justify-content: space-evenly;
  }
  .icon-tab svg { width: 20px; height: 20px; fill: var(--white); }
  .contact { position: absolute; left: 420px; top: 110px; color: var(--grey-text); }
  .contact .name { color: var(--orange); font-size: 23px; letter-spacing: 1px; }
  .contact .name b { font-weight: 900; }
  .contact .role { font-size: 16px; margin-top: 4px; }
  .contact .rule { width: 46px; height: 2px; background: var(--orange); margin: 10px 0 16px; }
  .contact p.line { font-size: 16px; line-height: 30px; }
</style>
</head>
<body>
  <section class="card card-back">
    <span class="tab tab-top"></span>
    <span class="tab tab-bottom"></span>
    <div class="brand"><span class="brand-dot"></span>VEMLO</div>
  </section>

  <section class="card card-front">
    <div class="panel"></div>
    <div class="brand"><span class="brand-dot"></span>VEMLO</div>
    <div class="icon-tab">
      <svg viewBox="0 0 24 24" aria-label="phone"><path d="M6.6 10.8a15 15 0 0 0 6.6 6.6l2.2-2.2a1 1 0 0 1 1-.25 11.4 11.4 0 0 0 3.6.57 1 1 0 0 1 1 1V20a1 1 0 0 1-1 1A17 17 0 0 1 3 4a1 1 0 0 1 1-1h3.5a1 1 0 0 1 1 1c0 1.25.2 2.45.57 3.57a1 1 0 0 1-.25 1z"/></svg>
      <svg viewBox="0 0 24 24" aria-label="email"><path d="M3 5h18v14H3z M3 5l9 7 9-7" fill="none" stroke="#fff" stroke-width="2"/></svg>
      <svg viewBox="0 0 24 24" aria-label="website"><path d="M4 3l16 7-7 2-2 7z"/></svg>
    </div>
    <div class="contact">
      <p class="name">DANIEL R. <b>WHITFORD</b></p>
      <p class="role">Managing Director</p>
      <div class="rule"></div>
      <p class="line">555.418.7290</p>
      <p class="line">companyname@mailbox.example</p>
      <p class="line">www.GuardedByVemlo.example</p>
    </div>
  </section>
</body>
</html>
```